updated website for children's organization
Riverbend Youth Network
updated website for children's organization  - Children
Creative Brief
Children
We are a state-wide coalition of child advocacy centers that provide services for children who have been abused. We are looking for a website design that goes along with our theme and illustrates that the work be do is for the children but also shows that we are a membership organization. In the future we would like our website to grow into something that can be used by the public as well as our members (separate members page). If you go to the link listed below you can learn a lot more about our organization. We purchased www.rbyouthnetwork.example but it's not live. The below link shows you want our current website looks like. https://web-rbyn.hostvale.example/
Clean, welcoming, not overwhelming
Modern
See our logo- main color blue
below header
http://www.plovermesa.example/
http://www.dunwickhub.example/
http://www.larkfieldyouthcircle.example/

```html
<!DOCTYPE html>
<html lang="en">
<head>
<meta charset="utf-8">
<title>Riverbend Youth Network</title>
<link href="https://fonts.googleapis.com/css2?family=Lato:wght@400;700;900&family=Comfortaa:wght@500;700&display=swap" rel="stylesheet">
<style>
:root{
  --blue:#2b86cf;
  --blue-dark:#1a6db5;
  --orange:#f28c28;
  --green:#6cb33f;
  --charcoal:#3a3a3a;
  --grey-band:#efefef;
  --text:#333;
  --muted:#555;
  --bottom:#2e2e2e;
}
*{margin:0;padding:0;box-sizing:border-box}
html,body{width:774px;height:1200px;overflow:hidden;background:#fff}
body{position:relative;font-family:'Lato',sans-serif;color:var(--text)}
.abs{position:absolute}
.round{font-family:'Comfortaa',sans-serif}

.brand{left:79px;top:18px;width:180px;display:flex;align-items:center;gap:8px}
.brand-dot{width:34px;height:34px;border-radius:50%;background:var(--orange);flex:none}
.brand-name{font-size:15px;font-weight:700;color:var(--blue-dark);line-height:1.15}
.top-btn{top:10px;height:23px;border-radius:12px;color:#fff;font-weight:900;font-size:9.5px;display:flex;align-items:center;gap:6px;padding-left:5px}
.top-btn .ic{width:15px;height:15px;border-radius:50%;background:rgba(255,255,255,.9);flex:none}
.btn-donate{left:338px;width:122px;background:var(--orange)}
.btn-login{left:467px;width:72px;background:var(--blue)}
.btn-register{left:546px;width:83px;background:var(--green)}
.btn-exit{left:637px;width:59px;background:var(--charcoal)}
.social-dot{top:55px;width:18px;height:18px;border-radius:50%;background:#4a4a4a}
.search{left:573px;top:52px;width:123px;height:23px;border:1px solid #ddd;border-radius:12px;font-size:8px;font-style:italic;color:#666;padding:6px 11px}
.search .go{position:absolute;right:3px;top:3px;width:15px;height:15px;border-radius:50%;background:#555}

.nav{left:0;top:94px;width:774px;height:35px;background:var(--blue)}
.nav-item{top:108px;font-size:11px;font-weight:700;color:#fff;letter-spacing:.2px}
.nav-home{left:79px;top:104px;width:57px;height:20px;border-radius:10px;background:var(--orange);color:#fff;font-size:11px;font-weight:900;text-align:center;line-height:20px}

.hero{left:0;top:129px;width:774px;height:314px;background:radial-gradient(ellipse at 48% 40%,#f0b66e 0%,#e08a2c 35%,#b9621b 70%,#8a4a1a 100%)}
.hero-label{left:505px;top:192px;width:199px;height:111px;background:rgba(70,52,35,.82);border-radius:3px}
.hero-title{left:516px;top:218px;font-size:19px;font-weight:900;color:#fff;line-height:23px}
.arrow{top:256px;width:22px;height:40px;background:rgba(60,50,40,.75)}
.arrow-l{left:0;border-radius:0 20px 20px 0}
.arrow-r{right:0;border-radius:20px 0 0 20px}
.cta{top:383px;height:38px;border-radius:3px;color:#fff;font-size:12px;font-weight:900;display:flex;align-items:center;gap:12px;padding-left:10px}
.cta .ic{width:26px;height:26px;border-radius:50%;background:#fff;flex:none}
.cta-donate{left:79px;width:140px;background:var(--orange)}
.cta-act{left:237px;width:140px;background:var(--blue)}
.cta-join{left:396px;width:140px;background:var(--green)}
.cta-advocate{left:555px;width:141px;background:var(--charcoal)}
.dots{left:356px;top:427px;width:63px;height:16px;background:#fff;border-radius:8px 8px 0 0;display:flex;justify-content:center;align-items:center;gap:4px}
.dots i{width:7px;height:7px;border-radius:50%;background:#555}
.dots i.on{background:var(--orange)}

.welcome-h{left:79px;top:463px;font-size:21px;font-weight:700;color:#222;letter-spacing:.5px}
.welcome-h b{color:var(--orange)}
.dotted{left:79px;top:497px;width:336px;border-top:2px dotted #ccc}
.lead{left:79px;top:511px;font-size:9.5px;font-weight:700;color:#333}
.bullet{left:79px;font-size:8.3px;font-weight:700;display:flex;align-items:center;gap:6px}
.bullet i{width:11px;height:11px;border-radius:50%;background:var(--blue);display:block}
.body-text{left:79px;top:591px;width:336px;font-size:7.4px;line-height:11px;color:var(--muted)}
.read-blue{left:79px;top:624px;width:76px;height:24px;background:var(--blue-dark);color:#fff;font-size:10px;font-weight:700;text-align:center;line-height:24px;border-radius:2px}
.video-card{left:434px;top:464px;width:262px;height:187px;background:#f2f2f2}
.video-frame{left:443px;top:472px;width:244px;height:126px;background:#fff;box-shadow:0 1px 3px rgba(0,0,0,.15)}
.video-art{left:449px;top:479px;width:231px;height:97px;background:linear-gradient(90deg,#f6b23b,#e8577a,#7fbf4a,#ee6b3b,#5fb7d6)}
.video-bar{left:449px;top:576px;width:231px;height:17px;background:#222}
.play{left:551px;top:514px;width:28px;height:28px}
.caption{left:445px;top:607px;font-size:10px;line-height:16px;color:#222;letter-spacing:.4px}

.band{left:0;top:679px;width:774px;height:237px;background:var(--grey-band)}
.figure{width:40px;height:110px;border-radius:20px 20px 4px 4px;background:linear-gradient(#e4e4e4,#dcdcdc)}
.card{top:700px;width:190px;height:189px;background:#fff;box-shadow:0 1px 3px rgba(0,0,0,.1)}
.card-head{top:700px;width:190px;height:30px;color:#fff;font-size:12px;font-weight:700;text-align:center;line-height:30px;letter-spacing:.6px}
.head-orange{background:var(--orange)}
.head-blue{background:var(--blue-dark)}
.head-green{background:var(--green)}
.card-btn{top:878px;width:77px;height:24px;color:#fff;font-size:9.5px;font-weight:700;text-align:center;line-height:24px;border-radius:2px}
.donate-intro{left:88px;top:742px;font-size:8.3px;font-weight:700;line-height:13px}
.field{left:89px;width:170px;height:22px;border:1px solid #ddd;border-radius:2px;font-size:7.5px;color:#555;padding:6px 8px}
.amount-label{left:91px;top:845px;font-size:7.8px;font-weight:700}
.select{left:131px;top:838px;width:64px;height:22px;border:1px solid #ddd;font-size:7.5px;padding:6px 7px}
.select .caret{position:absolute;right:0;top:0;width:14px;height:20px;border-left:1px solid #ddd;background:#f5f5f5}
.money{left:205px;top:838px;width:52px;height:22px;border:1px solid #ddd;font-size:7.5px;padding:6px 8px}
.volunteer-photo{left:301px;top:742px;width:173px;height:85px;background:linear-gradient(180deg,#c9c2b4 0%,#2f5fb4 55%,#27468c 100%)}
.vol-text{left:301px;top:838px;width:175px;font-size:7.3px;line-height:11px;color:var(--muted)}
.date{left:515px;width:35px;height:35px;background:var(--blue-dark);color:#fff;text-align:center}
.date small{display:block;height:9px;background:var(--green);font-size:5.5px;line-height:9px}
.date b{display:block;font-size:16px;line-height:26px}
.ev-title{left:557px;font-size:8.2px;font-weight:700;color:#222}
.ev-text{left:557px;width:135px;font-size:7.3px;line-height:11px;color:var(--muted)}

.partner{left:79px;top:942px;display:flex;align-items:center;gap:8px}
.partner .mark{width:56px;height:56px;border-radius:50%;background:#e9e9e9}
.partner .name{font-size:10px;color:#333;line-height:12px;text-align:center}
.vline{top:946px;height:68px;border-left:1px solid #e2e2e2}
.info-h{top:947px;font-size:11px;font-weight:700;color:#222}
.info-t{top:966px;font-size:7.8px;color:#333}
.phone{left:279px;top:980px;display:flex;align-items:center;gap:6px;font-size:11px;font-weight:700;color:#333}
.phone i{width:17px;height:17px;border-radius:50%;background:var(--blue);display:block}
.reg-btn{left:504px;top:979px;width:67px;height:19px;border-radius:10px;background:var(--blue);color:#fff;font-size:8px;font-weight:700;text-align:center;line-height:19px}

.footer{left:0;top:1024px;width:774px;height:146px;background:linear-gradient(135deg,#2f8ad0,#2274bb)}
.foot-h{top:1043px;font-size:11.5px;font-weight:700;color:#fff}
.foot-row{left:79px;display:flex;gap:8px;align-items:center;color:#fff;font-size:7.6px;font-weight:700;line-height:11px}
.foot-row i{width:22px;height:22px;border-radius:50%;background:#fff;display:block;flex:none}
.qlink{left:263px;font-size:7.6px;color:#fff}
.map{left:383px;top:1069px;width:165px;height:83px;background:linear-gradient(135deg,#ececec,#dcdcdc)}
.fdiv{top:1046px;height:110px;border-left:1px solid rgba(255,255,255,.2)}
.follow{left:594px;width:102px;height:18px;border:1px solid #fff;color:#fff;font-size:6.6px;font-weight:700;display:flex;align-items:center;gap:6px;padding-left:5px}
.follow i{width:9px;height:9px;background:#fff;display:block}
.bottom{left:0;top:1170px;width:774px;height:30px;background:var(--bottom);color:#ddd;font-size:7.4px}
.bottom .l{position:absolute;left:79px;top:11px}
.bottom .r{position:absolute;right:79px;top:11px}
</style>
</head>
<body>

<header>
  <div class="abs brand"><span class="brand-dot"></span><span class="brand-name">Riverbend Youth Network</span></div>
  <a class="abs top-btn btn-donate"><span class="ic"></span>MAKE DONATION</a>
  <a class="abs top-btn btn-login"><span class="ic"></span>LOGIN</a>
  <a class="abs top-btn btn-register"><span class="ic"></span>REGISTER</a>
  <a class="abs top-btn btn-exit"><span class="ic"></span>EXIT</a>
  <span class="abs social-dot" style="left:478px"></span>
  <span class="abs social-dot" style="left:501px"></span>
  <span class="abs social-dot" style="left:524px"></span>
  <span class="abs social-dot" style="left:547px"></span>
  <div class="abs search">Search here...<span class="go"></span></div>
</header>

<nav>
  <div class="abs nav"></div>
  <svg class="abs" style="left:0;top:89px" width="774" height="7" viewBox="0 0 774 7" aria-hidden="true">
    <path d="M0 7 Q4 1 8 7 T16 7 T24 7 T32 7 T40 7 T48 7 T56 7 T64 7 T72 7 T80 7 T88 7 T96 7 T104 7 T112 7 T120 7 T128 7 T136 7 T144 7 T152 7 T160 7 T168 7 T176 7 T184 7 T192 7 T200 7 T208 7 T216 7 T224 7 T232 7 T240 7 T248 7 T256 7 T264 7 T272 7 T280 7 T288 7 T296 7 T304 7 T312 7 T320 7 T328 7 T336 7 T344 7 T352 7 T360 7 T368 7 T376 7 T384 7 T392 7 T400 7 T408 7 T416 7 T424 7 T432 7 T440 7 T448 7 T456 7 T464 7 T472 7 T480 7 T488 7 T496 7 T504 7 T512 7 T520 7 T528 7 T536 7 T544 7 T552 7 T560 7 T568 7 T576 7 T584 7 T592 7 T600 7 T608 7 T616 7 T624 7 T632 7 T640 7 T648 7 T656 7 T664 7 T672 7 T680 7 T688 7 T696 7 T704 7 T712 7 T720 7 T728 7 T736 7 T744 7 T752 7 T760 7 T768 7 T776 7 Z" fill="#2b86cf"/>
  </svg>
  <span class="abs nav-home">HOME</span>
  <span class="abs nav-item" style="left:164px">ABOUT RYN</span>
  <span class="abs nav-item" style="left:260px">MEMBERS</span>
  <span class="abs nav-item" style="left:344px">GET INVOLVED</span>
  <span class="abs nav-item" style="left:455px">RECENT POST</span>
  <span class="abs nav-item" style="left:562px">BLOG</span>
  <span class="abs nav-item" style="left:622px">CONTACT US</span>
</nav>

<section>
  <div class="abs hero" role="img" aria-label="Photo of a smiling child lying in autumn leaves with a maple leaf on his head"></div>
  <div class="abs hero-label"></div>
  <h1 class="abs hero-title">HELP US A<br>CHILD THRIVE<br>NOT JUST SURVIVE</h1>
  <svg class="abs arrow arrow-l" viewBox="0 0 22 40" aria-hidden="true"><path d="M12 14 L6 20 L12 26" stroke="#fff" stroke-width="2" fill="none"/></svg>
  <svg class="abs arrow arrow-r" viewBox="0 0 22 40" aria-hidden="true"><path d="M10 14 L16 20 L10 26" stroke="#fff" stroke-width="2" fill="none"/></svg>
  <a class="abs cta cta-donate"><span class="ic"></span>DONATE NOW</a>
  <a class="abs cta cta-act"><span class="ic"></span>ACT NOW</a>
  <a class="abs cta cta-join"><span class="ic"></span>JOIN US</a>
  <a class="abs cta cta-advocate"><span class="ic"></span>ADVOCATE</a>
  <div class="abs dots"><i></i><i class="on"></i><i></i><i></i></div>
</section>

<section>
  <h2 class="abs welcome-h round">WELCOME TO <b>RYN</b></h2>
  <div class="abs dotted"></div>
  <p class="abs lead">Our Team Of Counselors Listen To And Stand With Child Victims:</p>
  <p class="abs bullet" style="top:532px"><i></i>When They Tell Their Story Of Abuse</p>
  <p class="abs bullet" style="top:551px"><i></i>Provide Counseling Sessions</p>
  <p class="abs bullet" style="top:570px"><i></i>And Prepare Families For A Court System That Can Be Frightening.</p>
  <p class="abs body-text">Lorem ipsum dolor sit amet, consectetur adipiscing elit. Nam sed maximus urna. Donec laci eget nulla vel ultricies. Nam ac laoreet ex. Aenean euismod vehicula erat semper egestas.</p>
  <a class="abs read-blue">Read More</a>

  <div class="abs video-card"></div>
  <div class="abs video-frame"></div>
  <div class="abs video-art" role="img" aria-label="Illustration of many colourful raised hands"></div>
  <div class="abs video-bar"></div>
  <svg class="abs play" viewBox="0 0 28 28" aria-hidden="true"><circle cx="14" cy="14" r="13" fill="rgba(30,30,30,.6)" stroke="#fff" stroke-width="1.5"/><path d="M11 9 L19 14 L11 19Z" fill="#fff"/></svg>
  <p class="abs caption round">THE CHILD ADVOCACY CENTER IS A PLACE<br>WHERE SMALL VOICES CAN BE HEARD.</p>
</section>

<section>
  <div class="abs band"></div>
  <div class="abs figure" style="left:16px;top:806px" role="img" aria-label="Faint silhouette of a girl"></div>
  <div class="abs figure" style="left:704px;top:800px;width:56px" role="img" aria-label="Faint silhouette of two children holding hands"></div>

  <div class="abs card" style="left:79px"></div>
  <h3 class="abs card-head head-orange round" style="left:79px">DONATE TODAY!</h3>
  <p class="abs donate-intro">Help HOPE Fight Poverty And Respond To<br>Desperate Need By Making A Donation</p>
  <div class="abs field" style="top:777px">Name:</div>
  <div class="abs field" style="top:807px">Email:</div>
  <span class="abs amount-label">Ammount</span>
  <div class="abs select">One Time<span class="caret"></span></div>
  <div class="abs money">$</div>
  <a class="abs card-btn" style="left:135px;background:var(--orange)">Donate Now</a>

  <div class="abs card" style="left:292px"></div>
  <h3 class="abs card-head head-blue round" style="left:292px">BECOME A VOLUNTEER</h3>
  <div class="abs volunteer-photo" role="img" aria-label="Photo of a smiling group of volunteers in blue shirts"></div>
  <p class="abs vol-text">Lorem ipsum dolor sit amet, consectet adipiscing elit. Praesent pretium massa ante, sit elementum lorem dapibus nec. Proin egestas lobortis.</p>
  <a class="abs card-btn" style="left:349px;background:var(--blue-dark)">Read More</a>

  <div class="abs card" style="left:505px"></div>
  <h3 class="abs card-head head-green round" style="left:505px">UPCOMING EVENTS</h3>
  <div class="abs date" style="top:742px"><small>November</small><b>22</b></div>
  <p class="abs ev-title" style="top:742px">LOREM IPSUM DOLOR SIT AMET</p>
  <p class="abs ev-text" style="top:755px">Mauris hendrerit aliquam co Mauris semper iaculis lacinialiqu euis.</p>
  <div class="abs date" style="top:787px"><small>November</small><b>24</b></div>
  <p class="abs ev-title" style="top:788px">LOREM IPSUM DOLOR SIT AMET</p>
  <p class="abs ev-text" style="top:801px">Mauris hendrerit aliquam co Mauris semper iaculis lacinialiqu euis.</p>
  <div class="abs date" style="top:833px"><small>November</small><b>26</b></div>
  <p class="abs ev-title" style="top:834px">LOREM IPSUM DOLOR SIT AMET</p>
  <p class="abs ev-text" style="top:847px">Mauris hendrerit aliquam co Mauris semper iaculis lacinialiqu euis.</p>
  <a class="abs card-btn" style="left:561px;background:var(--green)">Read More</a>
</section>

<section>
  <div class="abs partner"><span class="mark"></span><span class="name">COASTLINE<br>YOUTH FEDERATION</span></div>
  <div class="abs vline" style="left:245px"></div>
  <div class="abs vline" style="left:476px"></div>
  <h3 class="abs info-h" style="left:279px">IF YOU SUSPECT CHILD ABUSE</h3>
  <p class="abs info-t" style="left:280px">please call the Family Safety Line at</p>
  <p class="abs phone"><i></i>1-800-555-0142 or 911</p>
  <h3 class="abs info-h" style="left:504px">HOW TO REGISTER</h3>
  <p class="abs info-t" style="left:505px">Receive updateds from RYN by registering your email.</p>
  <a class="abs reg-btn">Register here</a>
</section>

<footer>
  <div class="abs footer"></div>
  <h4 class="abs foot-h" style="left:79px">GET IN TOUCH</h4>
  <div class="abs foot-row" style="top:1069px"><i></i><span>48 Millbrook Ave Suite<br>2-210 Riverton, ST 00000</span></div>
  <div class="abs foot-row" style="top:1099px"><i></i><span>Phone: (555) 014-2291<br>Fax: 555-014-2292</span></div>
  <div class="abs foot-row" style="top:1130px"><i></i><span>Email: info@rbyn.example<br>www.rbyouthnetwork.example</span></div>
  <div class="abs fdiv" style="left:236px"></div>
  <h4 class="abs foot-h" style="left:261px">QUICK LINKS</h4>
  <span class="abs qlink" style="top:1068px">›&nbsp; HOME</span>
  <span class="abs qlink" style="top:1087px">›&nbsp; ABOUT RYN</span>
  <span class="abs qlink" style="top:1106px">›&nbsp; MEMBERS</span>
  <span class="abs qlink" style="top:1125px">›&nbsp; GET INVOLVED</span>
  <span class="abs qlink" style="top:1144px">›&nbsp; CONTACT US</span>
  <div class="abs fdiv" style="left:359px"></div>
  <h4 class="abs foot-h" style="left:381px">OUR LOCATION</h4>
  <div class="abs map" role="img" aria-label="Street map showing the office location"></div>
  <div class="abs fdiv" style="left:573px"></div>
  <h4 class="abs foot-h" style="left:596px">FOLLOW US</h4>
  <a class="abs follow" style="top:1069px"><i></i>Follow us on Chatterbook</a>
  <a class="abs follow" style="top:1091px"><i></i>Follow us on Chirper</a>
  <a class="abs follow" style="top:1114px"><i></i>Follow us on ViewTube</a>
  <a class="abs follow" style="top:1136px"><i></i>Follow&nbsp; on Snapgram</a>
  <div class="abs bottom">
    <span class="l">© 2016 Riverbend Youth Network. All rights Reserved.</span>
    <span class="r">Privacy Policy &nbsp;&nbsp;|&nbsp;&nbsp; Terms of Use</span>
  </div>
</footer>

</body>
</html>
```